Manufacturer of prepared Persian ready meals needs a product concept design

I need a product concept design for a new company based in the UK called 'Valdor Foods Ltd'.
The winner will potentially be selected to produce prototype designs for our other products.
For this project, the product will be called "Ghormeh Sabzi". This needs to be on the design to let consumers know what it is.
Whilst still in the concept stage, the aim of the company is to produce refrigerated microwaveable / oven Persian ready meal for retail supermarket consumers, and may also have an online platform for direct to consumer sales.
I have provided quite a few competitor examples of products.
I would like the product in a black or clear round bowl. It will be split into two sections (Half stew / Half rice) by the sleeve, which you are designing. I would like the food to be visible on either side of the label, so the consumer knows what they are eating.
The logo is provided within the file attachments and needs to be on prominent display on the pouch.
The mission for Valdor Foods Ltd brand is:
"Bringing 2,500 years of scented history to your table".
This needs to be present on the sleeve.
The product needs to represent the ethnicity of the brand throughout the design, and the same font to be used throughout.
Persian architecture was filled with a wide range of vibrant colours and has been engineered to stand the test of time, so I would like that to be incorporated into the product design (see attached examples of Persian geometry).
Alternatively Persian carpets are world renowned for their quality, so examples of this could be displayed on the packaging.
These will have to be artistically interpreted to avoid potential copyright; I am looking for individual artistic design.
It needs to represent a super quality, royalty & decadence throughout, and stand out on the shelves to the consumer above all the other competitor products.
To comply with food standards, the sleeve must have a nutritional label on display. I have attached a generic example for you to use. You may create your own representation of it.
Ghormeh Sabzi is a natural source of fibre, high in protein, gluten and dairy free, so I would like this displayed on the sleeve, as well as the the words:
- Traditionally rich in aromatic herbs, tender slow cooked lamb, red kidney beans & dried limes
- One of the oldest dishes in Persian history
You can find pictures of the food provided in the files. Note, these are not my pictures, but give you an idea of what will be provided inside.
Some designers have uploaded the same design up to 5 times, others twice. Only 18 have been uploaded, but it says 20, so I think 2 have been removed?

```html
<!DOCTYPE html>
<html lang="en">
<head>
<meta charset="utf-8">
<title>Valdor Foods – Ghormeh Sabzi sleeve</title>
<link rel="stylesheet" href="https://fonts.googleapis.com/css2?family=Montserrat:ital,wght@0,300;0,400;0,600;1,600&family=Bebas+Neue&family=Roboto+Condensed:wght@400;700&display=swap">
<style>
  :root {
    --orange-top: #df5521;
    --orange-bottom: #ef5b25;
    --pattern-tone: #f27a2e;
    --yellow: #fff200;
    --white: #ffffff;
    --ink: #1e1e1e;
    --green: #5cb947;
    --red: #e8472a;
    --amber: #f6a532;
    --badge-green: #1aa24a;
    --canvas: #ffffff;
  }
  * { box-sizing: border-box; margin: 0; padding: 0; }
  html, body { width: 1200px; height: 1200px; overflow: hidden; background: var(--canvas); }
  .stage { position: relative; width: 1200px; height: 1200px; }
  .sleeve {
    position: absolute; left: 214px; top: 115px;
    width: 772px; height: 970px;
    transform: scale(0.95); transform-origin: center;
    background: linear-gradient(180deg, var(--orange-top) 0%, var(--orange-bottom) 45%, var(--orange-bottom) 100%);
    overflow: hidden;
    font-family: "Montserrat", sans-serif; color: var(--white);
  }
  .pattern-field {
    position: absolute; left: 0; right: 0; top: 440px; bottom: 0;
    background: radial-gradient(ellipse at 50% 60%, rgba(242,122,46,0.55) 0%, rgba(242,122,46,0.25) 50%, rgba(242,122,46,0) 80%);
  }
  .brand-mark {
    position: absolute; left: 330px; top: 100px; width: 112px; height: 112px;
    border: 6px solid var(--white);
  }
  .brand-name {
    position: absolute; left: 0; right: 0; top: 286px; text-align: center;
    font-weight: 400; color: var(--white); line-height: 1;
  }
  .brand-name .primary { display: block; font-size: 84px; letter-spacing: 40px; padding-left: 40px; }
  .brand-name .secondary { display: block; font-size: 36px; letter-spacing: 18px; padding-left: 18px; margin-top: 4px; }
  .mission {
    position: absolute; left: 0; right: 0; top: 426px; text-align: center;
    font-style: italic; font-weight: 600; font-size: 17px;
  }
  .product-title { position: absolute; left: 40px; top: 500px; width: 690px; height: 140px; }
  .product-title text { font-family: "Bebas Neue", sans-serif; fill: var(--yellow); }
  .description {
    position: absolute; left: 0; right: 0; top: 638px; text-align: center;
    font-weight: 300; font-size: 20px; line-height: 24px;
  }
  .heritage {
    position: absolute; left: 0; right: 0; top: 725px; text-align: center;
    font-style: italic; font-weight: 600; font-size: 19px; color: var(--ink);
  }
  .info-panel {
    position: absolute; left: 181px; top: 801px; width: 410px; height: 175px;
    background: var(--white); border-radius: 22px 22px 0 0; color: var(--ink);
    font-family: "Roboto Condensed", sans-serif;
  }
  .nutrition { position: absolute; left: 26px; top: 22px; width: 230px; text-align: center; }
  .nutrition .lead { font-size: 10.5px; }
  .traffic-lights { display: flex; justify-content: center; gap: 1px; margin-top: 6px; }
  .light {
    width: 35px; height: 62px; border: 1px solid #333; border-radius: 0 0 12px 12px;
    display: flex; flex-direction: column; align-items: center; font-size: 8px; line-height: 1.1;
    padding-top: 2px; position: relative;
  }
  .light .value { font-size: 12px; font-weight: 700; }
  .light .level { background: var(--white); font-size: 7px; font-weight: 700; padding: 0 3px; margin-top: 3px; }
  .light .ri { position: absolute; bottom: 1px; font-size: 11px; }
  .light.energy { background: var(--white); font-size: 7.5px; }
  .light.green { background: var(--green); }
  .light.red { background: var(--red); }
  .light.amber { background: var(--amber); }
  .nutrition .foot { font-size: 10px; margin-top: 6px; line-height: 1.35; }
  .claims { position: absolute; left: 271px; top: 22px; width: 120px; display: grid; grid-template-columns: 52px 52px; gap: 6px 8px; }
  .claim {
    width: 52px; height: 52px; border-radius: 50%; border: 3px solid var(--badge-green);
    color: var(--badge-green); font-family: "Montserrat", sans-serif; font-weight: 600;
    font-size: 6.5px; line-height: 1.15; display: flex; align-items: center; justify-content: center; text-align: center;
  }
</style>
</head>
<body>
<main class="stage">
  <section class="sleeve">
    <div class="pattern-field" role="img" aria-label="Fine Persian carpet-style ornamental line pattern in lighter orange"></div>

    <div class="brand-mark"></div>
    <h1 class="brand-name"><span class="primary">VALDOR</span><span class="secondary">FOODS</span></h1>
    <p class="mission">Bringing 2,500 years of scented history to your table</p>

    <svg class="product-title" viewBox="0 0 690 140" aria-label="Ghormeh Sabzi">
      <text x="0" y="127" font-size="172" textLength="688" lengthAdjust="spacingAndGlyphs">GHORMEH SABZI</text>
    </svg>

    <p class="description">Traditionally rich in aromatic herbs, tender slow cooked lamb,<br>red kidney beans &amp; dried limes</p>
    <p class="heritage">One of the oldest dishes in Persian history</p>

    <div class="info-panel">
      <div class="nutrition">
        <p class="lead">Each serving (150g) contains</p>
        <div class="traffic-lights">
          <div class="light energy">Energy<br>1046kJ<br>250kcal<span class="ri">13%</span></div>
          <div class="light green">Fat<span class="value">3.0g</span><span class="level">LOW</span><span class="ri">4%</span></div>
          <div class="light green">Saturates<span class="value">1.3g</span><span class="level">LOW</span><span class="ri">7%</span></div>
          <div class="light red">Sugars<span class="value">34g</span><span class="level">HIGH</span><span class="ri">38%</span></div>
          <div class="light amber">Salt<span class="value">0.9g</span><span class="level">MED</span><span class="ri">15%</span></div>
        </div>
        <p class="foot">of an adult's reference intake<br>Typical values (as sold) per 100g: 697kJ/ 167kcal</p>
      </div>
      <div class="claims">
        <div class="claim">NATURAL<br>SOURCE<br>OF FIBRE</div>
        <div class="claim">HIGH IN<br>PROTEIN</div>
        <div class="claim">DAIRY<br>FREE</div>
        <div class="claim">GLUTEN<br>FREE</div>
      </div>
    </div>
  </section>
</main>
</body>
</html>
```